Private Investigator needs a Business Card design

We provide Private Investigator Service on demand. I can provide any type of logo format you may want. Our website is www.korvale.com. I DONT want a spy glass, nor an eye, nor a barnaby quill. I DO want creative and professional.

Our service focus is GPS tracking, surveillance, infidelity, business investigations.

Target Market(s)

Attorneys, Professionals, Insurance Companies

Industry/Entity Type

Business

Contact Information for Business Card

Will vary per the business card holder. Here is a sample. Feel free to use icons if you like instead of phone...etc. (((SEE ATTACHMENT))

DORIAN MALKOVETZ
Director of Investigations/Founder

Office: 855-KorVale (567-8253) Direct: 727-555-0142
Cell: 727-555-0187 Email: dorian@KorVale.com
Web: KorVale.com Lic #D7392816
218 W. Birch Ave. Tampa, Fl. 33681

Colors
3176b5
1461a9
0492cd
33a6d7

Requirements
Must have
• I DO want creative and professional. I like the Zelto look.
• We would like to have some space on the back that we may put notes.
Should not have
• I DONT want a spy glass, nor an eye, nor a barnaby quill.
• No clear and no black cards.

```html
<!DOCTYPE html>
<html lang="en">
<head>
<meta charset="utf-8">
<title>KorVale Business Cards</title>
<link href="https://fonts.googleapis.com/css2?family=Montserrat:wght@500;700;800&display=swap" rel="stylesheet">
<style>
  :root{
    --royal:#2747ad;
    --royal-deep:#1d3795;
    --brand:#1461a9;
    --sky:#33a6d7;
    --ink:#1d2b55;
    --paper:#ffffff;
    --stage:#ececec;
    --mist:#e9ecf3;
    --badge:#e3b62a;
  }
  *{box-sizing:border-box;margin:0;padding:0}
  html,body{width:776px;height:1200px;overflow:hidden}
  body{background:var(--stage);font-family:'Montserrat',Arial,sans-serif;position:relative;color:var(--ink)}
  .card{position:absolute;border-radius:12px;overflow:hidden;background:var(--paper);box-shadow:0 2px 6px rgba(0,0,0,.12)}
  .card--blue{background:var(--royal)}
  .wordmark{display:flex;align-items:center;gap:8px;font-weight:800;letter-spacing:-.5px;color:var(--royal);white-space:nowrap}
  .wordmark .dot{border-radius:50%;background:currentColor;flex:none}
  .card--blue .wordmark{color:#fff}
  .name{font-weight:800;font-size:12px;letter-spacing:.3px;color:var(--royal-deep);white-space:nowrap}
  .title{font-weight:500;font-size:7.5px;color:var(--ink);margin-top:2px;white-space:nowrap}
  .contacts{list-style:none;margin-top:7px}
  .contacts li{display:flex;align-items:center;gap:5px;font-size:7px;font-weight:500;line-height:13px;white-space:nowrap}
  .contacts i{width:8px;height:8px;border-radius:50%;background:var(--royal);flex:none}
  .badge{position:absolute;width:40px;height:14px;border-radius:3px;background:var(--badge)}
  .mark-zone{position:absolute;border-radius:50%;background:var(--mist)}
  .card--blue .mark-zone{background:rgba(255,255,255,.08)}
  .band{position:absolute;right:0;top:0;width:150px;height:100%;background:var(--royal);clip-path:polygon(30% 0,100% 0,100% 100%,0 100%)}
  .band-accent{position:absolute;top:0;width:8px;height:100%;background:var(--sky);transform:skewX(-8deg);transform-origin:top}
  .band-tint{position:absolute;border-radius:10px;background:rgba(255,255,255,.1)}
  .cols{display:flex;gap:22px}
  .cols .contacts li{font-size:6px;line-height:11px}
  .cols .contacts i{width:6px;height:6px}
</style>
</head>
<body>

<section class="card card--blue" style="left:207px;top:70px;width:432px;height:196px">
  <div class="mark-zone" role="img" aria-label="Faint brand emblem" style="left:270px;top:-30px;width:200px;height:200px"></div>
  <div class="wordmark" style="position:absolute;left:110px;top:70px;font-size:46px">
    <span class="dot" style="width:22px;height:22px"></span>KorVale
  </div>
</section>

<section class="card" style="left:207px;top:279px;width:432px;height:213px">
  <div class="band"></div>
  <div class="band-accent" style="left:270px"></div>
  <div class="band-tint" role="img" aria-label="Brand emblem area" style="left:335px;top:24px;width:80px;height:80px"></div>
  <div style="position:absolute;left:20px;top:22px">
    <div class="name">DORIAN MALKOVETZ</div>
    <div class="title">Director of Investigations/Founder</div>
    <ul class="contacts">
      <li><i></i>855-KorVale (567-8253)</li>
      <li><i></i>727-555-0142</li>
      <li><i></i>727-555-0187</li>
      <li><i></i>dorian@KorVale.com</li>
      <li><i></i>KorVale.com</li>
      <li><i></i>218 W. Birch Ave. Tampa, Fl 33681</li>
      <li><i></i>Lic #D7392816</li>
    </ul>
  </div>
  <div class="badge" style="left:100px;top:188px"></div>
</section>

<section class="card" style="left:207px;top:502px;width:432px;height:202px">
  <div class="mark-zone" role="img" aria-label="Faint brand emblem" style="left:270px;top:10px;width:180px;height:180px"></div>
  <div class="wordmark" style="position:absolute;left:26px;top:28px;font-size:38px">
    <span class="dot" style="width:18px;height:18px"></span>KorVale
  </div>
  <div style="position:absolute;left:26px;top:92px">
    <div class="name" style="font-size:10px">DORIAN MALKOVETZ</div>
    <div class="title" style="font-size:6px">Director of Investigations/Founder</div>
    <div class="cols">
      <ul class="contacts">
        <li><i></i>855-KorVale (567-8253)</li>
        <li><i></i>727-555-0142</li>
        <li><i></i>727-555-0187</li>
      </ul>
      <ul class="contacts">
        <li><i></i>dorian@KorVale.com</li>
        <li><i></i>KorVale.com</li>
        <li><i></i>218 W. Birch Ave. Tampa, Fl 33681</li>
      </ul>
      <ul class="contacts">
        <li><i></i>Lic #D7392816</li>
      </ul>
    </div>
  </div>
  <div class="badge" style="left:300px;top:170px"></div>
</section>

<section class="card card--blue" style="left:65px;top:737px;width:189px;height:432px">
  <div class="mark-zone" role="img" aria-label="Faint brand emblem" style="left:20px;top:120px;width:200px;height:200px"></div>
  <div class="wordmark" style="position:absolute;left:22px;top:196px;font-size:30px">
    <span class="dot" style="width:14px;height:14px"></span>KorVale
  </div>
</section>

<section class="card" style="left:279px;top:737px;width:213px;height:432px">
  <div class="mark-zone" role="img" aria-label="Faint brand emblem" style="left:40px;top:150px;width:200px;height:200px"></div>
  <div class="wordmark" style="position:absolute;left:30px;top:60px;font-size:32px">
    <span class="dot" style="width:15px;height:15px"></span>KorVale
  </div>
  <div style="position:absolute;left:26px;top:130px">
    <div class="name">DORIAN MALKOVETZ</div>
    <div class="title">Director of Investigations/Founder</div>
    <ul class="contacts">
      <li><i></i>855-KorVale (567-8253)</li>
      <li><i></i>727-555-0142</li>
      <li><i></i>727-555-0187</li>
      <li><i></i>dorian@KorVale.com</li>
      <li><i></i>KorVale.com</li>
      <li><i></i>218 W. Birch Ave. Tampa, Fl 33681</li>
      <li><i></i>Lic #D7392816</li>
    </ul>
  </div>
  <div class="badge" style="left:86px;top:380px"></div>
</section>

<section class="card" style="left:512px;top:737px;width:192px;height:432px">
  <div class="mark-zone" role="img" aria-label="Faint brand emblem" style="left:30px;top:130px;width:190px;height:190px"></div>
  <div class="wordmark" style="position:absolute;left:22px;top:78px;font-size:30px">
    <span class="dot" style="width:14px;height:14px"></span>KorVale
  </div>
  <div style="position:absolute;left:22px;top:140px">
    <div class="name" style="font-size:11px">DORIAN MALKOVETZ</div>
    <div class="title">Director of Investigations/Founder</div>
    <ul class="contacts">
      <li><i></i>855-KorVale (567-8253)</li>
      <li><i></i>727-555-0142</li>
      <li><i></i>727-555-0187</li>
      <li><i></i>dorian@KorVale.com</li>
      <li><i></i>KorVale.com</li>
      <li><i></i>218 W. Birch Ave. Tampa, Fl 33681</li>
      <li><i></i>Lic #D7392816</li>
    </ul>
  </div>
  <div class="badge" style="left:120px;top:380px"></div>
</section>

</body>
</html>
```